Tidewell Outdoor Signage

We need an outdoor signage design for my company with new logo designed from makerhive. We do electrical, Air conditioning & Plumbing, installation, service, repairs and maintenance. The design shall be an eye catching that cannot miss ready it.

Industry/Entity Type

Electrical, Air conditioning, Plumbing

```html
<!DOCTYPE html>
<html lang="en">
<head>
<meta charset="utf-8">
<title>Tidewell Outdoor Signage</title>
<link rel="stylesheet" href="https://fonts.googleapis.com/css2?family=Poppins:wght@600;700&display=swap">
<style>
  :root {
    --page: #eef0f2;
    --white: #ffffff;
    --red: #e32027;
    --red-deep: #c1161d;
    --orange: #ef8a3c;
    --blue: #1b64ab;
    --blue-light: #2a86c9;
    --photo-a: #d7e0ea;
    --photo-b: #33507a;
  }
  html, body {
    margin: 0;
    width: 1200px;
    height: 1117px;
    overflow: hidden;
    background: var(--page);
    font-family: "Poppins", sans-serif;
  }
  .sign {
    position: absolute;
    left: 20px;
    top: 251px;
    width: 1160px;
    height: 615px;
    background: var(--white);
    overflow: hidden;
  }
  .sign-shapes {
    position: absolute;
    inset: 0;
  }
  .brand-name {
    position: absolute;
    left: 58px;
    top: 232px;
    margin: 0;
    font-size: 124px;
    font-weight: 700;
    line-height: 1;
    letter-spacing: -2px;
    color: var(--orange);
  }
  .service-line {
    position: absolute;
    left: 56px;
    top: 395px;
    margin: 0;
    display: flex;
    gap: 18px;
    font-size: 25px;
    font-weight: 700;
    line-height: 1;
  }
  .service-line .electrical { color: var(--red); }
  .service-line .air { color: var(--blue); }
  .service-line .plumbing { color: var(--orange); }
  .services-band {
    position: absolute;
    left: 200px;
    right: 60px;
    top: 486px;
    margin: 0;
    text-align: center;
    color: var(--white);
    font-size: 35px;
    font-weight: 600;
    line-height: 1.2;
  }
</style>
</head>
<body>
  <main class="sign">
    <svg class="sign-shapes" width="1160" height="615" viewBox="0 0 1160 615" aria-hidden="false">
      <defs>
        <linearGradient id="band-fill" x1="0" y1="0" x2="1" y2="1">
          <stop offset="0" stop-color="var(--blue)"/>
          <stop offset="0.7" stop-color="var(--blue)"/>
          <stop offset="1" stop-color="var(--blue-light)"/>
        </linearGradient>
        <linearGradient id="corner-fill" x1="0" y1="0" x2="1" y2="1">
          <stop offset="0" stop-color="var(--red-deep)"/>
          <stop offset="0.4" stop-color="var(--red)"/>
        </linearGradient>
        <radialGradient id="photo-fill" cx="0.45" cy="0.45" r="0.7">
          <stop offset="0" stop-color="var(--photo-a)"/>
          <stop offset="1" stop-color="var(--photo-b)"/>
        </radialGradient>
      </defs>

      <path class="corner-swoosh" d="M0 0 H250 C120 60 30 180 0 330 Z" fill="url(#corner-fill)"/>

      <path class="services-band-shape" d="M0 475 C90 470 150 462 185 455 L1160 450 V615 H0 Z" fill="url(#band-fill)"/>

      <path class="tick" d="M0 508 L52 538 L174 445 C120 458 80 490 50 575 L0 515 Z" fill="var(--white)"/>
      <path class="tick" d="M4 512 L50 548 L165 450 C115 470 78 505 48 565 Z" fill="var(--red)"/>

      <circle cx="846" cy="266" r="172" fill="var(--white)"/>
      <circle cx="846" cy="266" r="158" fill="url(#photo-fill)" role="img" aria-label="Photo of a technician's hands holding an air conditioning pressure gauge manifold"/>
    </svg>

    <h1 class="brand-name">Tidewell</h1>
    <p class="service-line">
      <span class="electrical">Electrical</span>
      <span class="air">Air Conditioning</span>
      <span class="plumbing">Plumbing</span>
    </p>
    <p class="services-band">Electrical • AC &amp; Plumbing • Installation • service<br>• repairs and maintenance</p>
  </main>
</body>
</html>
```